Spice Mix Label Bottle Branding - Health and Weight Loss Mixes

The company is called ZestRow Spice Mix's. We've created 5 spice mixes using ingredients that promote health and weight loss. We already have a logo but now we need labels for our bottles. We would like to see designs that have the feel of health supplements (see attached examples)

We would like a different colour featured with each of our flavours.

Our flavours are:
-Golden Chai (Yellow)
-Mild Curry (Orange)
-Coffee Rub (brown)
-Garlic Oregano (Green)
-Taco (Blue)

Thank you!

Target Market(s)

Ages 22-35. Men and Female. Trendy, Hipster.

Industry/Entity Type

Food Production

Font styles to use
Sans Serif

Colors
f37122
0655a3
0692cd
9bcb3c
fbee3f

Requirements
Must have
• A different featured colour for each flavour.
• The ZestRow Spices Logo (attached)
• The slogan: "Weight Loss Ingredients"
• -Golden Chai (Yellow)
• -Mild Curry (Orange)
• -Coffee Rub (brown)
• -Garlic Oregano (Green)
• -Taco (Blue)
• Text Files attached.
Nice to have
• A black label with a featured colour for each of the spice mice flavours.
• 'No Salt added'

```html
<!DOCTYPE html>
<html lang="en">
<head>
<meta charset="utf-8">
<title>ZestRow Spices – Label Range</title>
<link href="https://fonts.googleapis.com/css2?family=Oswald:wght@400;500;700&display=swap" rel="stylesheet">
<style>
  :root {
    --page: #f4f4f6;
    --label: #1d1d1d;
    --ink-light: #ffffff;
    --logo-ink: #1d1d1d;
    --coffee: #a87a52;
    --coffee-dark: #7a5535;
    --curry: #f37122;
    --curry-dark: #b94d10;
    --chai: #e6be2a;
    --chai-dark: #a8850f;
    --garlic: #9bcb3c;
    --garlic-dark: #6c9222;
    --taco: #3d8bea;
    --taco-dark: #0655a3;
  }
  * { box-sizing: border-box; margin: 0; padding: 0; }
  html, body {
    width: 1200px; height: 849px; overflow: hidden;
    background: var(--page);
    font-family: "Oswald", "Arial Narrow", sans-serif;
  }
  .range {
    position: absolute; left: 50px; top: 250px;
    display: flex; gap: 30px; align-items: flex-start;
  }
  .label {
    position: relative;
    width: 196px; height: 300px;
    background: var(--label);
    display: flex; flex-direction: column; align-items: center;
    color: var(--ink-light);
  }
  .label--coffee { --accent: var(--coffee); --accent-dark: var(--coffee-dark); }
  .label--curry  { --accent: var(--curry);  --accent-dark: var(--curry-dark); }
  .label--chai   { --accent: var(--chai);   --accent-dark: var(--chai-dark); }
  .label--garlic { --accent: var(--garlic); --accent-dark: var(--garlic-dark); }
  .label--taco   { --accent: var(--taco);   --accent-dark: var(--taco-dark); }

  .brand {
    width: 74px; height: 60px; background: var(--ink-light);
    display: flex; flex-direction: column; align-items: center; justify-content: center; gap: 4px;
  }
  .brand-mark { width: 10px; height: 10px; background: var(--logo-ink); }
  .brand-name {
    font-weight: 700; font-size: 15px; color: var(--logo-ink); line-height: 1;
  }
  .slogan {
    position: relative; width: 186px; height: 30px; margin-top: -10px;
  }
  .slogan svg { position: absolute; inset: 0; }
  .slogan .band { fill: var(--accent); }
  .slogan .tail { fill: var(--accent-dark); }
  .slogan-text {
    position: absolute; inset: 0 0 8px 0;
    display: flex; align-items: center; justify-content: center;
    font-size: 10px; font-weight: 500; color: var(--ink-light); letter-spacing: 0.2px;
  }
  .flavour {
    flex: 1; display: flex; align-items: center; justify-content: center;
    text-align: center; font-weight: 700; font-size: 40px; line-height: 1.05;
    text-transform: uppercase; letter-spacing: 1px;
    text-shadow: 2px 2px 0 var(--accent);
    padding: 0 8px;
  }
  .claim {
    display: flex; align-items: center; gap: 8px;
    font-size: 9px; color: var(--accent); margin-bottom: 18px;
  }
  .claim::before, .claim::after {
    content: ""; width: 44px; height: 1px; background: var(--accent);
  }
  .net {
    font-size: 7px; color: var(--ink-light); letter-spacing: 0.5px; margin-bottom: 16px;
  }
</style>
</head>
<body>
<main class="range">

  <article class="label label--coffee">
    <div class="brand"><span class="brand-mark"></span><span class="brand-name">ZestRow</span></div>
    <div class="slogan">
      <svg viewBox="0 0 186 30" preserveAspectRatio="none" aria-hidden="true">
        <polygon class="tail" points="0,8 18,8 18,26 0,26 7,17"/>
        <polygon class="tail" points="186,8 168,8 168,26 186,26 179,17"/>
        <polygon class="band" points="12,2 174,2 174,22 12,22"/>
      </svg>
      <span class="slogan-text">Weight Loss Ingredients</span>
    </div>
    <h2 class="flavour">Coffee<br>Rub</h2>
    <p class="claim">No Salt added</p>
    <p class="net">NET SIZE 3OZ</p>
  </article>

  <article class="label label--curry">
    <div class="brand"><span class="brand-mark"></span><span class="brand-name">ZestRow</span></div>
    <div class="slogan">
      <svg viewBox="0 0 186 30" preserveAspectRatio="none" aria-hidden="true">
        <polygon class="tail" points="0,8 18,8 18,26 0,26 7,17"/>
        <polygon class="tail" points="186,8 168,8 168,26 186,26 179,17"/>
        <polygon class="band" points="12,2 174,2 174,22 12,22"/>
      </svg>
      <span class="slogan-text">Weight Loss Ingredients</span>
    </div>
    <h2 class="flavour">Mild<br>Curry</h2>
    <p class="claim">No Salt added</p>
    <p class="net">NET SIZE 3OZ</p>
  </article>

  <article class="label label--chai">
    <div class="brand"><span class="brand-mark"></span><span class="brand-name">ZestRow</span></div>
    <div class="slogan">
      <svg viewBox="0 0 186 30" preserveAspectRatio="none" aria-hidden="true">
        <polygon class="tail" points="0,8 18,8 18,26 0,26 7,17"/>
        <polygon class="tail" points="186,8 168,8 168,26 186,26 179,17"/>
        <polygon class="band" points="12,2 174,2 174,22 12,22"/>
      </svg>
      <span class="slogan-text">Weight Loss Ingredients</span>
    </div>
    <h2 class="flavour">Golden<br>Chai</h2>
    <p class="claim">No Salt added</p>
    <p class="net">NET SIZE 3OZ</p>
  </article>

  <article class="label label--garlic">
    <div class="brand"><span class="brand-mark"></span><span class="brand-name">ZestRow</span></div>
    <div class="slogan">
      <svg viewBox="0 0 186 30" preserveAspectRatio="none" aria-hidden="true">
        <polygon class="tail" points="0,8 18,8 18,26 0,26 7,17"/>
        <polygon class="tail" points="186,8 168,8 168,26 186,26 179,17"/>
        <polygon class="band" points="12,2 174,2 174,22 12,22"/>
      </svg>
      <span class="slogan-text">Weight Loss Ingredients</span>
    </div>
    <h2 class="flavour">Garlic<br>Oregano</h2>
    <p class="claim">No Salt added</p>
    <p class="net">NET SIZE 3OZ</p>
  </article>

  <article class="label label--taco">
    <div class="brand"><span class="brand-mark"></span><span class="brand-name">ZestRow</span></div>
    <div class="slogan">
      <svg viewBox="0 0 186 30" preserveAspectRatio="none" aria-hidden="true">
        <polygon class="tail" points="0,8 18,8 18,26 0,26 7,17"/>
        <polygon class="tail" points="186,8 168,8 168,26 186,26 179,17"/>
        <polygon class="band" points="12,2 174,2 174,22 12,22"/>
      </svg>
      <span class="slogan-text">Weight Loss Ingredients</span>
    </div>
    <h2 class="flavour">Taco</h2>
    <p class="claim">No Salt added</p>
    <p class="net">NET SIZE 3OZ</p>
  </article>

</main>
</body>
</html>
```